Tolvane Logo & Packaging Design

I need a logo and packaging label for a roll-on deodorant. I have a design in mind, however it needs to be changed to suit the information based in the design brief.

The logo and product label should be a point of differentiation, to help the brand stand out from the masses.

I have attached a detailed brief with all required information, so please review carefully.

Target Market(s)

Modern man working professional, 24-35, $70K+ income, stays fit and healthy

Industry/Entity Type

Hair And Beauty

Requirements
Must have
• colour, bold typeface, logo and graphic.
• please see this landing page for idea reference: http://www.quillhollowtaps.com/our-ales/
• https://cdn1.pixelharbor.net/static/71cd9a22f3c14b0e93a27d58/t/6b293f5635b705217c4e1bc9/1622645315366/KRT
• https://cdn1.pixelharbor.net/static/71cd9a22f3c14b0e93a27d58/t/606808d47b5a74ed79d3e40a/1509023834683/?format=750w
Should not have
• no black and white only.

```html
<!DOCTYPE html>
<html lang="en">
<head>
<meta charset="utf-8">
<title>Tolvane Roll-On Label</title>
<link rel="stylesheet" href="https://fonts.googleapis.com/css2?family=Cinzel:wght@400;700&display=swap">
<style>
  :root {
    --stage-blue: #2a80dc;
    --label-black: #121214;
    --label-black-soft: #1c1c20;
    --brand-blue: #2a3fae;
    --dot-blue: rgba(52, 86, 214, 0.75);
    --text-light: #e9e9ec;
  }
  html, body {
    margin: 0;
    padding: 0;
    width: 1200px;
    height: 1200px;
    overflow: hidden;
    background: var(--stage-blue);
  }
  .canvas {
    position: relative;
    width: 1200px;
    height: 1200px;
    background: var(--stage-blue);
  }
  .label {
    position: absolute;
    left: 330px;
    top: 200px;
    width: 540px;
    height: 800px;
    background: linear-gradient(180deg, var(--label-black-soft), var(--label-black) 50%, var(--label-black-soft));
    overflow: hidden;
  }
  .pattern {
    position: absolute;
    left: 0;
    width: 100%;
  }
  .pattern--top {
    top: 0;
    height: 300px;
    background: linear-gradient(180deg, var(--dot-blue) 0%, rgba(52, 86, 214, 0.25) 45%, rgba(52, 86, 214, 0) 100%);
  }
  .pattern--bottom {
    bottom: 0;
    height: 360px;
    background: linear-gradient(0deg, var(--dot-blue) 0%, rgba(52, 86, 214, 0.3) 45%, rgba(52, 86, 214, 0) 100%);
  }
  .brand {
    position: absolute;
    left: 50%;
    top: 160px;
    transform: translateX(-50%);
    width: 420px;
    height: 82px;
    background: var(--brand-blue);
    display: flex;
    align-items: center;
    justify-content: center;
  }
  .brand__name {
    font-family: 'Cinzel', serif;
    font-weight: 700;
    font-size: 52px;
    letter-spacing: 3px;
    color: var(--text-light);
    text-transform: uppercase;
  }
  .product {
    position: absolute;
    left: 0;
    top: 330px;
    width: 100%;
    text-align: center;
    font-family: 'Cinzel', serif;
    font-weight: 400;
    color: var(--text-light);
  }
  .product__line {
    margin: 0;
    font-size: 34px;
    letter-spacing: 3px;
    line-height: 1.22;
  }
  .product__joiner {
    margin: 10px 0 14px;
    font-size: 15px;
    letter-spacing: 2px;
  }
  .volume {
    position: absolute;
    left: 50%;
    bottom: 28px;
    transform: translateX(-50%);
    padding: 4px 16px;
    border-radius: 8px;
    background: #1a2a7a;
    font-family: 'Cinzel', serif;
    font-weight: 400;
    font-size: 15px;
    letter-spacing: 2px;
    color: var(--text-light);
  }
</style>
</head>
<body>
  <main class="canvas">
    <section class="label">
      <div class="pattern pattern--top" role="img" aria-label="Blue diamond halftone pattern fading downward"></div>
      <div class="pattern pattern--bottom" role="img" aria-label="Blue diamond halftone pattern fading upward"></div>

      <div class="brand">
        <span class="brand__name">Tolvane</span>
      </div>

      <div class="product">
        <p class="product__line">Fantastic</p>
        <p class="product__line">Deodorant</p>
        <p class="product__joiner">WITH</p>
        <p class="product__line">New Range</p>
      </div>

      <div class="volume">75 ML</div>
    </section>
  </main>
</body>
</html>
```